I need three graphics made that will go on walls in a basketball lockerroom

I need three graphics made that will go on a basketball lockerroom wall. Here are the specifics.
Graphic 1 (Size 115" wide by 52" tall, min 150 DPI)
This should be something that displays the acronym for TOLVAR. The main background color should be the teal color attached. Use logos and the other approved colors as needed.
Standards
Intensity
Effort
Grit
Energy
Love
Graphic 2 (Size 88" wide by 52" tall, min 150 DPI)
This one should be on the Navy Blue background color attached
and impactful way say Attitude and Effort
Graphic 3 (Size 100" wide by 18" tall, min 150 DPI)
This goes along the top of the way and needs to say
(THS logo) Stars Lead the Way (Star logo) Tolvar Basketball (THS logo)
All three of these need to feel like they are of the same style. For Graphic #2 I thought something maybe like the attached basketball except use the S Star in the middle and say attitude and effort using the colors .. but I'm open to other ideas

```html
<!DOCTYPE html>
<html lang="en">
<head>
<meta charset="utf-8">
<title>Tolvar Basketball Locker Room Graphics</title>
<link rel="stylesheet" href="https://fonts.googleapis.com/css2?family=Saira+Condensed:wght@800;900&display=swap">
<style>
  :root {
    --teal: #17858a;
    --teal-light: #22a3ad;
    --teal-deep: #0f6f74;
    --navy: #1f3358;
    --navy-dark: #182a4a;
    --silver: #b9bcbf;
    --white: #ffffff;
  }
  html, body {
    margin: 0;
    padding: 0;
    width: 1200px;
    height: 800px;
    overflow: hidden;
    background: var(--white);
  }
  .canvas {
    position: relative;
    width: 1200px;
    height: 800px;
    font-family: "Saira Condensed", "Arial Narrow", sans-serif;
  }
  .banner { position: absolute; overflow: hidden; }

  /* Graphic 1: values wall */
  .values-wall {
    left: 42px; top: 82px; width: 670px; height: 303px;
    background: linear-gradient(160deg, var(--teal-deep) 0%, var(--teal) 35%, var(--teal-light) 60%, var(--teal) 100%);
  }
  .value-word {
    position: absolute;
    transform: translate(-50%, -50%) rotate(var(--tilt));
    font-weight: 900;
    font-style: italic;
    color: var(--silver);
    -webkit-text-stroke: 1.5px var(--navy);
    letter-spacing: 0.5px;
    white-space: nowrap;
    line-height: 1;
  }
  .ball-splash {
    position: absolute;
    left: 245px; top: 35px; width: 210px; height: 215px;
    border-radius: 50%;
    background: radial-gradient(circle at 55% 50%, var(--navy) 0%, var(--navy) 55%, rgba(31,51,88,0.4) 72%, rgba(31,51,88,0) 78%);
  }
  .team-mark {
    position: absolute;
    transform: translate(-50%, -50%);
    font-weight: 900;
    color: var(--silver);
    line-height: 1;
    white-space: nowrap;
  }
  .mark-dot {
    position: absolute;
    width: 30px; height: 30px;
    border-radius: 50%;
    background: var(--navy);
    transform: translate(-50%, -50%);
  }

  /* Graphic 2: attitude & effort */
  .attitude-wall {
    left: 42px; top: 407px; width: 528px; height: 311px;
    background: var(--navy);
  }
  .court-backdrop {
    position: absolute;
    left: 51px; top: 31px; width: 423px; height: 258px;
    background: radial-gradient(ellipse at center, rgba(120,140,175,0.22) 0%, rgba(120,140,175,0.08) 70%, rgba(120,140,175,0) 100%);
    border: 1px solid rgba(150,165,195,0.35);
  }
  .slogan {
    position: absolute;
    left: 0; width: 100%;
    text-align: center;
    transform: translateY(-50%);
    font-weight: 900;
    font-style: italic;
    color: var(--teal);
    -webkit-text-stroke: 2px var(--silver);
    line-height: 1;
    letter-spacing: -1px;
  }
  .slogan-main { font-size: 72px; }
  .slogan-amp { font-size: 58px; }

  /* Graphic 3: top strip */
  .header-strip {
    left: 585px; top: 610px; width: 596px; height: 107px;
    background: var(--teal);
  }
  .strip-balls {
    position: absolute;
    left: 182px; top: 24px; width: 225px; height: 62px;
    border-radius: 31px;
    background: linear-gradient(90deg, rgba(24,42,74,0.9) 0%, rgba(24,42,74,0.35) 40%, rgba(24,42,74,0.35) 60%, rgba(24,42,74,0.9) 100%);
  }
</style>
</head>
<body>
<main class="canvas">

  <section class="banner values-wall" aria-label="Tolvar values banner">
    <span class="value-word" style="left:96px; top:60px; font-size:40px; --tilt:8deg;">GRIT</span>
    <span class="value-word" style="left:143px; top:124px; font-size:32px; --tilt:-15deg;">STANDARDS</span>
    <span class="value-word" style="left:112px; top:234px; font-size:38px; --tilt:10deg;">ENERGY</span>
    <span class="value-word" style="left:552px; top:70px; font-size:40px; --tilt:-8deg;">EFFORT</span>
    <span class="value-word" style="left:571px; top:154px; font-size:32px; --tilt:12deg;">LOVE</span>
    <span class="value-word" style="left:539px; top:240px; font-size:38px; --tilt:-14deg;">INTENSITY</span>
    <div class="ball-splash" role="img" aria-label="Navy paint splash with basketball illustration"></div>
    <span class="mark-dot" style="left:340px; top:52px;"></span>
    <span class="team-mark" style="left:340px; top:211px; font-size:66px;">THS</span>
  </section>

  <section class="banner attitude-wall" aria-label="Attitude and effort banner">
    <div class="court-backdrop" role="img" aria-label="Faint basketball court diagram"></div>
    <span class="slogan slogan-main" style="top:109px;">ATTITUDE</span>
    <span class="slogan slogan-amp" style="top:165px;">&amp;</span>
    <span class="slogan slogan-main" style="top:221px;">EFFORT</span>
  </section>

  <section class="banner header-strip" aria-label="Tolvar Basketball header strip">
    <span class="team-mark" style="left:91px; top:56px; font-size:56px;">THS</span>
    <div class="strip-balls" role="img" aria-label="Two basketball illustrations flanking a star"></div>
    <span class="team-mark" style="left:501px; top:56px; font-size:56px;">THS</span>
  </section>

</main>
</body>
</html>
```